Overview of Elder Abuse Resources Brochure

We need a 2-page brochure that provides a list of resources for elders in tribal communities in the US and those who care for them. We want it to be simple and easy to read, and easy to see the difference between each resource. We would also like eye-catching images or graphics. Please keep the images on the front, and add any photos or graphics that depict Native American elders. We need both of our logos on the first page, in the far-right column. Please refer to the attached image for our brand colors and a font suggestion. Please keep the three columns on each page, but delete the blank pages in the document.

```html
<!DOCTYPE html>
<html lang="en">
<head>
<meta charset="utf-8">
<title>Services for Elders &amp; People Who Care for Them – Brochure</title>
<link href="https://fonts.googleapis.com/css2?family=Barlow:ital,wght@0,400;0,500;0,600;0,700;1,500;1,600&family=Barlow+Condensed:wght@600;700&display=swap" rel="stylesheet">
<style>
:root{
  --red:#b4524b;
  --red-soft:#c98a85;
  --teal:#4e9ea6;
  --slate:#7b878b;
  --sky:#e3eef0;
  --ink:#2f3234;
  --stage:#646565;
  --white:#ffffff;
  --band:linear-gradient(90deg,#7e8b8f 0%,#9a7a76 55%,#b4524b 100%);
  --card-head:linear-gradient(90deg,#4e9ea6 0%,#8a8581 60%,#b4524b 100%);
}
*{box-sizing:border-box;margin:0;padding:0}
html,body{width:1200px;height:1200px;overflow:hidden}
body{background:var(--stage);font-family:"Barlow",Arial,sans-serif;color:var(--ink);position:relative}
.sheet{position:absolute;left:223px;width:753px;height:580px;box-shadow:0 6px 18px rgba(0,0,0,.35)}
.sheet--outside{top:10px}
.sheet--inside{top:610px}
.page{position:absolute;left:0;top:0;width:845px;height:651px;transform:scale(.8911);transform-origin:0 0;background:var(--white);overflow:hidden}
.col{position:absolute;top:0;height:621px}
.col--sky{background:linear-gradient(180deg,#e6f0f2 0%,#dfecee 100%)}
.border-band{position:absolute;left:0;bottom:0;width:845px;height:30px;background:linear-gradient(90deg,#7e9a9f,#a97a74,#7e9a9f,#a97a74,#7e9a9f,#a97a74)}
.band{background:var(--band);color:var(--white);font-family:"Barlow Condensed","Barlow",sans-serif;font-weight:700;text-transform:uppercase;line-height:.98}
.band--title{height:52px;padding:7px 16px 0;font-size:23px;margin-top:16px}
.band--plain{text-transform:none;font-family:"Barlow",sans-serif;font-weight:600;font-size:19px;height:40px;padding:9px 16px 0}
.body{font-size:10.5px;line-height:1.3;padding:0 16px}
.body p{margin-top:6px}
.accent{color:var(--red);font-style:italic;font-weight:600}
.red{color:var(--red)}
.teal{color:var(--teal);font-weight:600}
.contact-box{margin:8px 6px 0;border:1px solid var(--red-soft);padding:8px 8px 6px;font-size:9.5px}
.contact-box div{display:flex;gap:3px;margin-bottom:6px}
.contact-box span.line{flex:1;border-bottom:1px solid #999;margin-bottom:2px}
.emergency{margin:22px 16px 0;height:34px;border:1.5px solid var(--white);outline:1px solid var(--red-soft);background:linear-gradient(90deg,#7e9a9f,#b4524b);color:var(--white);font-family:"Barlow Condensed",sans-serif;font-weight:700;font-size:18px;display:flex;align-items:center;justify-content:center}
.wordmark{font-family:"Barlow",sans-serif;font-weight:700;color:var(--red);text-transform:uppercase;line-height:1}
.wordmark--small{font-size:11px;text-align:right}
.wordmark--mid{font-size:16px}
.wordmark--gold{color:#d7a566;font-size:17px;text-align:center}
.dot{display:inline-block;width:12px;height:12px;background:var(--teal);border-radius:50%;vertical-align:middle;margin-right:6px}
.vertical{position:absolute;writing-mode:vertical-rl;transform:rotate(180deg)}
.addr{left:18px;bottom:18px;font-size:11.5px;line-height:1.15;white-space:nowrap}
.addr .wordmark{font-size:13px;font-weight:600}
.contact-vert{left:240px;bottom:18px;font-size:11.5px;font-weight:500;white-space:nowrap;display:flex;gap:6px}
.contact-vert .gap{height:70px}
.photo{background:radial-gradient(ellipse at 55% 40%,#a37067 0%,#6e2f3d 45%,#3a2624 100%)}
.photo--hands{background:radial-gradient(ellipse at 50% 55%,#c99b84 0%,#9f7563 40%,#e9e3de 100%)}
.names{background:var(--teal);color:var(--white);font-size:12px;font-weight:500;text-align:center;line-height:1.3;padding:4px 0;height:38px}
.cover-title{background:linear-gradient(135deg,#b4524b 0%,#a5493f 100%);color:var(--white);font-family:"Barlow Condensed",sans-serif;font-weight:700;font-size:24px;line-height:1;padding:12px 20px;height:97px;text-transform:uppercase}
.squares{list-style:none;padding:10px 18px 0;font-size:10px;font-weight:500}
.squares li{position:relative;padding-left:14px;margin-bottom:5px}
.squares li::before{content:"";position:absolute;left:0;top:3px;width:6px;height:6px;background:var(--teal)}
.arrows{list-style:none;padding:14px 16px 0 18px;font-size:12px;font-weight:500;line-height:1.3}
.arrows li{position:relative;padding-left:18px;margin-bottom:10px}
.arrows svg{position:absolute;left:0;top:3px;width:12px;height:9px}
.help{color:var(--red);font-family:"Barlow Condensed",sans-serif;font-weight:700;font-size:29px;line-height:.9;padding:4px 18px 0}
.card{margin:10px 16px 0 18px;border:1.2px solid var(--red-soft);background:var(--white);border-radius:2px}
.card h3{background:var(--card-head);color:var(--white);font-size:13.5px;font-weight:600;line-height:1.1;padding:3px 10px}
.card .txt{font-size:10.2px;line-height:1.22;padding:5px 10px 5px}
.card .rule{border-top:1px dashed #b9b9b9;margin:4px 10px 2px}
.card .item{display:flex;align-items:center;gap:6px;font-size:10.2px;color:var(--red);padding:0 10px;line-height:1.25}
.card .item:last-child{padding-bottom:4px}
.card .link{color:var(--red);display:block}
.ic{width:9px;height:9px;flex:none}
.sub{color:var(--red);font-style:italic;font-weight:600;font-size:18px;text-align:center;margin-top:8px}
.kin{text-align:center;font-size:11px;font-weight:600;line-height:1.2;margin-top:2px}
</style>
</head>
<body>
<svg width="0" height="0" style="position:absolute" aria-hidden="true">
  <defs>
    <symbol id="i-mail" viewBox="0 0 12 12"><rect x="1" y="2.5" width="10" height="7" fill="none" stroke="#b4524b" stroke-width="1.3"/><path d="M1 3l5 4 5-4" fill="none" stroke="#b4524b" stroke-width="1.3"/></symbol>
    <symbol id="i-phone" viewBox="0 0 12 12"><path d="M3 1l2 2.5-1.2 1.3c.7 1.5 1.9 2.7 3.4 3.4L8.5 7 11 9l-1.3 1.8C5.5 10.5 1.5 6.5 1.2 2.3z" fill="#b4524b"/></symbol>
    <symbol id="i-globe" viewBox="0 0 12 12"><circle cx="6" cy="6" r="4.8" fill="none" stroke="#b4524b" stroke-width="1.2"/><path d="M1.2 6h9.6M6 1.2c-2.5 3-2.5 6.6 0 9.6M6 1.2c2.5 3 2.5 6.6 0 9.6" fill="none" stroke="#b4524b" stroke-width="1"/></symbol>
    <symbol id="i-arrow" viewBox="0 0 12 9"><path d="M0 0l5 4.5L0 9zM6 0l5 4.5L6 9z" fill="#4e9ea6"/></symbol>
  </defs>
</svg>

<!-- Outside spread -->
<section class="sheet sheet--outside">
  <div class="page">
    <div class="col" style="left:0;width:278px">
      <h2 class="band band--title">Respect for<br>Elders</h2>
      <div class="body">
        <p>Do you have concerns about an Elder, maybe you see that they are not taking care of themselves, or family only comes once a month when the Elder has money?</p>
        <p>Is an Elder telling you that they are not treated with respect or that someone is bothering them?</p>
        <p class="accent">These may be signs of Elder abuse, neglect or exploitation</p>
      </div>
      <h2 class="band band--plain" style="margin-top:18px">For help contact:</h2>
      <div class="body">
        <p style="margin-top:10px;font-size:9.5px">Your Tribal Social Services or Elders Department:</p>
        <div class="contact-box">
          <div>Contact:<span class="line"></span></div>
          <div>Phone:<span class="line"></span></div>
        </div>
        <p style="margin-top:20px;font-size:11.5px">The Elder Help Finder for information on Adult Protective Services<br><span class="red">1-800-555-0116</span></p>
      </div>
      <div class="emergency">IF A SERIOUS EMERGENCY, CALL 911</div>
      <div class="body" style="font-size:11.5px">
        <p style="margin-top:16px">For mental health support for yourself or an Elder, <span class="teal">call or text 555-0188</span></p>
        <p style="margin-top:12px">Family Safety Hotline<br>1.800.555.0172</p>
      </div>
    </div>

    <div class="col col--sky" style="left:278px;width:284px">
      <div style="position:absolute;right:20px;top:22px;width:150px">
        <div class="wordmark wordmark--small"><span class="dot"></span>Northwind Council<br>on Elder Care</div>
      </div>
      <div class="vertical addr">
        <div class="wordmark">Northwind Council<br>on Elder Care</div>
        <div>48 Birchwood Ave. #12<br>Riverton, ST 00000</div>
      </div>
      <div class="vertical contact-vert">
        <span><svg class="ic" style="transform:rotate(90deg)"><use href="#i-phone"/></svg> (555) 214-0187</span>
        <span class="gap"></span>
        <span><svg class="ic"><use href="#i-globe"/></svg> northwindelders.org<br><svg class="ic"><use href="#i-mail"/></svg> finder@elderhelpline.org</span>
      </div>
    </div>

    <div class="col" style="left:562px;width:283px">
      <div class="photo" style="height:265px" role="img" aria-label="Photograph of a Native American elder woman in a headscarf and blanket being cared for by another elder"></div>
      <div class="names">My Mother • My Father • My Sister<br>My Grandchild • Myself</div>
      <h1 class="cover-title">Services for Elders<br>&amp; People Who Care<br>for Them</h1>
      <ul class="squares">
        <li>Are you caring for an Elder or a Grandchild?</li>
        <li>Are you an Elder who needs help staying at home?</li>
        <li>These programs and information can be a helpful resource.</li>
      </ul>
      <div style="padding:10px 0 0 28px" class="wordmark wordmark--mid"><span class="dot"></span>Northwind Council on Elder Care</div>
      <div style="padding-top:22px" class="wordmark wordmark--gold">Cedar Elder<br>Justice Project</div>
    </div>
    <div class="border-band" role="img" aria-label="Decorative zigzag border pattern in teal and brick red"></div>
  </div>
</section>

<!-- Inside spread -->
<section class="sheet sheet--inside">
  <div class="page">
    <div class="col" style="left:0;width:284px">
      <h2 class="band band--title">Do these stories<br>sound familiar to you?</h2>
      <ul class="arrows">
        <li><svg><use href="#i-arrow"/></svg>My mother gets lost driving home from the store.</li>
        <li><svg><use href="#i-arrow"/></svg>I need help getting groceries and with chores at home.</li>
        <li><svg><use href="#i-arrow"/></svg>My dad wants to sleep all the time; he doesn't go out with friends anymore. He stopped drumming.</li>
        <li><svg><use href="#i-arrow"/></svg>My sister is raising 3 grandchildren on her own.</li>
        <li><svg><use href="#i-arrow"/></svg>My son is disrespecting me. He only comes to visit when my retirement money arrives. He always asks for money.</li>
      </ul>
      <p class="help">HELP IS<br>AVAILABLE...</p>
      <div class="photo photo--hands" style="position:absolute;left:0;bottom:0;width:284px;height:213px" role="img" aria-label="Close-up photograph of an elder's folded, weathered hands"></div>
    </div>

    <div class="col col--sky" style="left:284px;width:283px">
      <h2 class="band band--title">Resources for<br>Elders</h2>
      <div class="card">
        <h3>Elder Help Finder</h3>
        <div class="txt">For help finding support.<br>Ask about services to Tribal Elders.</div>
        <div class="rule"></div>
        <div class="item"><svg class="ic"><use href="#i-mail"/></svg>elderhelpfinder.org/home</div>
        <div class="item"><svg class="ic"><use href="#i-phone"/></svg>1-800-555-0116</div>
        <div class="item"><svg class="ic"><use href="#i-globe"/></svg>help@elderhelpfinder.org</div>
      </div>
      <div class="card">
        <h3>Memory Care Help Line</h3>
        <div class="txt"><i>(24 hours 7 days a week)</i><br>For support for people living with dementia, caregivers, families and the public. Connect with a live person who can provide information, local resources, crisis assistance and emotional support.</div>
        <div class="item"><svg class="ic"><use href="#i-phone"/></svg>1-800-555-0390</div>
      </div>
      <div class="card">
        <h3>Crisis Support Line</h3>
        <div class="txt">For mental health support,<br>call or text 555-0188.</div>
      </div>
      <div class="card">
        <h3>State &amp; Tribal Hotlines | Cedar Elder Justice Project</h3>
        <div class="txt">To find local resources within your tribe or state that specialize in elder abuse, neglect or exploitation, visit:<span class="link">https://northwindelders.org/cedar/hotlines/ state-tribal-hotlines/</span></div>
      </div>
      <div class="card">
        <h3>Kinship Native Helpline</h3>
        <div class="txt">A 24/7 safe, confidential and anonymous domestic and sexual violence helpline for Native Americans and Alaska Natives</div>
        <div class="item"><svg class="ic"><use href="#i-phone"/></svg>1-800-555-0148</div>
        <div class="item"><span class="ic"></span>(1-800-555-KIN1)</div>
        <div class="item"><svg class="ic"><use href="#i-globe"/></svg>kinshiphelpline.org</div>
      </div>
    </div>

    <div class="col" style="left:567px;width:278px">
      <h2 class="band band--title">Resources for<br>Caregivers</h2>
      <p class="sub">Caring for an Older Adult</p>
      <div class="card">
        <h3>Elder Help Finder</h3>
        <div class="txt">For help finding support.<br>Ask about services to Tribal Elders.</div>
        <div class="rule"></div>
        <div class="item"><svg class="ic"><use href="#i-mail"/></svg>elderhelpfinder.org/home</div>
        <div class="item"><svg class="ic"><use href="#i-phone"/></svg>1-800-555-0116</div>
        <div class="item"><svg class="ic"><use href="#i-globe"/></svg>help@elderhelpfinder.org</div>
      </div>
      <div class="card">
        <h3>Memory Friends | Northwind Council on Elder Care</h3>
        <div class="txt">An interactive educational program to better understand what dementia is and how it affects people.<span class="link">https://northwindelders.org/memory-friends/</span></div>
      </div>
      <p class="sub" style="margin-top:16px">Caring for a Grandchild</p>
      <p class="kin">Grandparents Raising<br>Grandchildren (Kinship Care)</p>
      <div class="card">
        <h3>Kinfamilies.org</h3>
        <div class="txt">An interactive website that seeks to share all relevant publicly available information impacting grandfamilies.</div>
      </div>
      <div class="card">
        <h3>Grandparent Resources | Cedar Elder Justice Project</h3>
        <div class="txt">A list of resources for grandparents raising grandchildren.<span class="link">https://northwindelders.org/cedar/resource/grand parent-resources/</span></div>
      </div>
    </div>
    <div class="border-band" role="img" aria-label="Decorative zigzag border pattern in teal and brick red"></div>
  </div>
</section>
</body>
</html>
```